Fire Hydrant Repair Parts Flyer

We need a flyer advertising both fire hydrant parts and the manufacturers that we are stocking. Our company is Coastal Flowline Supply and we are a parts distributor who sells directly to contractors. I have attached an example flyer that advertises some other parts we stock. We don't want it to look exactly like the old flyer, but we would like it to be structured similarly. I have also attached a background image for the flyer as well as some pictures of the parts we are stocking. I have also attached pictures of the manufacturer logos that we are stocking. We are trying to convey the parts that we are stocking which are: "Traffic Repair Kits", "Main Valve Repair Kits", "Extension Kits", "Replacement Caps & Gaskets", "Replacement Nozzles", Adjustable Hydrant Wrenches", "Hydrant Diffusers", & "Hydrant Oil". I have attached pictures of some of these items that we would like placed on the flyer. Let me know if you have any questions at all.

```html
<!DOCTYPE html>
<html lang="en">
<head>
<meta charset="utf-8">
<title>Fire Pump Repair – Parts and Accessories</title>
<link href="https://fonts.googleapis.com/css2?family=Montserrat:wght@400;500;600;700;800&display=swap" rel="stylesheet">
<style>
  :root {
    --page-bg: #e9ecef;
    --navy: #3a4ea3;
    --royal: #2e3f9c;
    --pink: #ec1c5a;
    --magenta: #d1206a;
    --soft: #eeeff3;
    --ink: #1f2230;
    --white: #ffffff;
    --brand-red: #b3202a;
    --brand-green: #1f7a3a;
    --brand-grey: #7a7d85;
  }
  * { box-sizing: border-box; margin: 0; padding: 0; }
  html, body { width: 1200px; height: 1031px; overflow: hidden; }
  body {
    background: var(--page-bg);
    font-family: "Montserrat", sans-serif;
    position: relative;
  }
  .flyer {
    position: absolute;
    left: 255px; top: 31px;
    width: 690px; height: 968px;
    background: var(--soft);
    overflow: hidden;
    box-shadow: 0 10px 30px rgba(0,0,0,.18);
  }
  .hero {
    position: absolute; left: 0; top: 0;
    width: 690px; height: 490px;
    background: linear-gradient(180deg, var(--navy) 0%, var(--magenta) 22%, var(--pink) 40%, var(--pink) 100%);
  }
  .hero svg { position: absolute; left: 0; top: 0; }
  .title {
    position: absolute; left: 0; top: 22px; width: 100%;
    text-align: center; color: var(--white);
    font-weight: 800; font-size: 56px; letter-spacing: 0.5px; line-height: 1;
  }
  .subtitle {
    position: absolute; left: 0; top: 84px; width: 100%;
    text-align: center; color: var(--white);
    font-weight: 700; font-size: 29px; letter-spacing: 0.5px; line-height: 1;
  }
  .products-photo {
    position: absolute; left: 325px; top: 500px;
    width: 345px; height: 275px;
    border-radius: 12px;
    background: radial-gradient(closest-side, #d4d7dd 0%, #dfe1e6 60%, rgba(238,239,243,0) 100%);
  }
  .parts-list {
    position: absolute; left: 47px; top: 512px;
    list-style: none;
  }
  .parts-list li {
    display: flex; align-items: center; gap: 8px;
    height: 33.8px;
    font-size: 15.5px; font-weight: 500; color: var(--ink);
  }
  .parts-list svg { flex: none; }
  .makers {
    position: absolute; left: 0; top: 785px;
    width: 100%; height: 70px; background: var(--white);
    display: flex; align-items: center; justify-content: space-around;
    padding: 0 22px;
  }
  .maker { font-size: 14px; font-weight: 700; line-height: 1.1; }
  .maker--harlow { color: var(--brand-red); }
  .maker--ridgeline { color: var(--brand-red); }
  .maker--kestrel { color: var(--brand-green); }
  .maker--summit { color: var(--brand-grey); }
  .maker--norland { color: var(--ink); font-size: 24px; font-weight: 800; }
  .company {
    position: absolute; left: 0; top: 855px;
    width: 100%; height: 65px; background: var(--white);
    display: flex; align-items: center; justify-content: center; gap: 12px;
  }
  .company-mark { width: 22px; height: 22px; background: var(--royal); }
  .company-name { color: var(--royal); font-size: 29px; font-weight: 500; }
  .footer {
    position: absolute; left: 0; top: 920px;
    width: 100%; height: 48px;
  }
  .footer svg.band { position: absolute; left: 0; top: 0; }
  .footer-call, .footer-web {
    position: absolute; top: 0; height: 48px;
    display: flex; align-items: center; gap: 6px;
    color: var(--white); font-size: 17px;
  }
  .footer-call { left: 26px; font-weight: 600; }
  .footer-call strong, .footer-web strong { font-weight: 700; }
  .footer-web { right: 20px; }
</style>
</head>
<body>
<main class="flyer">
  <section class="hero">
    <svg width="690" height="490" viewBox="0 0 690 490">
      <defs>
        <linearGradient id="streetScene" x1="0" y1="0" x2="0" y2="1">
          <stop offset="0" stop-color="#8a8e98"/>
          <stop offset="0.35" stop-color="#7f8b5e"/>
          <stop offset="0.6" stop-color="#d8dbe0"/>
          <stop offset="1" stop-color="#6e8f48"/>
        </linearGradient>
      </defs>
      <path d="M0 170 C120 150 200 235 330 205 C450 178 560 120 690 145 L690 175 C560 150 450 205 330 232 C200 258 120 185 0 200 Z" fill="#ffffff" opacity="0.9"/>
      <path d="M0 182 C120 165 200 245 330 218 C450 192 560 140 690 160" fill="none" stroke="#3a4ea3" stroke-width="8"/>
      <path d="M0 195 C120 180 200 255 330 228 C450 202 560 150 690 172 L690 442 C600 430 520 400 430 410 C300 425 200 470 120 455 C70 445 30 440 0 448 Z"
            fill="url(#streetScene)" role="img" aria-label="Photo of a red fire hydrant releasing a strong stream of water onto a street lawn"/>
      <path d="M0 452 C30 446 70 452 120 462 C200 478 300 432 430 418 C520 408 600 438 690 450 L690 490 L0 490 Z" fill="#eeeff3"/>
      <path d="M0 448 C30 440 70 445 120 455 C200 470 300 425 430 410 C520 400 600 430 690 442" fill="none" stroke="#ec1c5a" stroke-width="4"/>
      <path d="M0 456 C30 450 70 456 120 466 C200 482 300 436 430 422 C520 412 600 442 690 454" fill="none" stroke="#3a4ea3" stroke-width="3" opacity="0.8"/>
    </svg>
    <h1 class="title">FIRE PUMP REPAIR</h1>
    <p class="subtitle">PARTS AND ACCESSORIES</p>
  </section>

  <div class="products-photo" role="img" aria-label="Product photos: hydrant diffuser with gauge, nozzle cap with chain, hydrant wrench, bottle of hydrant oil, traffic and extension repair kits"></div>

  <ul class="parts-list">
    <li><svg width="12" height="12" viewBox="0 0 12 12"><circle cx="6" cy="6" r="6" fill="#3a4ea3"/><circle cx="6" cy="6" r="4.6" fill="#ec1c5a"/><path d="M3.4 6.2 L5.2 8 L8.6 4.3" fill="none" stroke="#fff" stroke-width="1.5"/></svg>Traffic Repair Kits</li>
    <li><svg width="12" height="12" viewBox="0 0 12 12"><circle cx="6" cy="6" r="6" fill="#3a4ea3"/><circle cx="6" cy="6" r="4.6" fill="#ec1c5a"/><path d="M3.4 6.2 L5.2 8 L8.6 4.3" fill="none" stroke="#fff" stroke-width="1.5"/></svg>Main Valve Repair Kits</li>
    <li><svg width="12" height="12" viewBox="0 0 12 12"><circle cx="6" cy="6" r="6" fill="#3a4ea3"/><circle cx="6" cy="6" r="4.6" fill="#ec1c5a"/><path d="M3.4 6.2 L5.2 8 L8.6 4.3" fill="none" stroke="#fff" stroke-width="1.5"/></svg>Extension Kits</li>
    <li><svg width="12" height="12" viewBox="0 0 12 12"><circle cx="6" cy="6" r="6" fill="#3a4ea3"/><circle cx="6" cy="6" r="4.6" fill="#ec1c5a"/><path d="M3.4 6.2 L5.2 8 L8.6 4.3" fill="none" stroke="#fff" stroke-width="1.5"/></svg>Replacement Caps &amp; Gaskets</li>
    <li><svg width="12" height="12" viewBox="0 0 12 12"><circle cx="6" cy="6" r="6" fill="#3a4ea3"/><circle cx="6" cy="6" r="4.6" fill="#ec1c5a"/><path d="M3.4 6.2 L5.2 8 L8.6 4.3" fill="none" stroke="#fff" stroke-width="1.5"/></svg>Replacement Nozzles</li>
    <li><svg width="12" height="12" viewBox="0 0 12 12"><circle cx="6" cy="6" r="6" fill="#3a4ea3"/><circle cx="6" cy="6" r="4.6" fill="#ec1c5a"/><path d="M3.4 6.2 L5.2 8 L8.6 4.3" fill="none" stroke="#fff" stroke-width="1.5"/></svg>Adjustable Hydrant Wrenches</li>
    <li><svg width="12" height="12" viewBox="0 0 12 12"><circle cx="6" cy="6" r="6" fill="#3a4ea3"/><circle cx="6" cy="6" r="4.6" fill="#ec1c5a"/><path d="M3.4 6.2 L5.2 8 L8.6 4.3" fill="none" stroke="#fff" stroke-width="1.5"/></svg>Hydrant Diffusers</li>
    <li><svg width="12" height="12" viewBox="0 0 12 12"><circle cx="6" cy="6" r="6" fill="#3a4ea3"/><circle cx="6" cy="6" r="4.6" fill="#ec1c5a"/><path d="M3.4 6.2 L5.2 8 L8.6 4.3" fill="none" stroke="#fff" stroke-width="1.5"/></svg>Hydrant Oil</li>
  </ul>

  <section class="makers">
    <span class="maker maker--harlow">Harlow Valve</span>
    <span class="maker maker--ridgeline">Ridgeline Pipe</span>
    <span class="maker maker--kestrel">Kestrel Valve</span>
    <span class="maker maker--summit">Summit Flow Control</span>
    <span class="maker maker--norland">NORLAND</span>
  </section>

  <section class="company">
    <span class="company-mark"></span>
    <span class="company-name">Coastal Flowline Supply</span>
  </section>

  <footer class="footer">
    <svg class="band" width="690" height="48" viewBox="0 0 690 48">
      <rect width="690" height="48" fill="#3a4ea3"/>
      <path d="M0 0 H360 C395 0 410 20 428 48 H0 Z" fill="#ec1c5a"/>
    </svg>
    <div class="footer-call">Call Us Today!
      <svg width="16" height="16" viewBox="0 0 24 24"><path d="M6.6 10.8a15 15 0 0 0 6.6 6.6l2.2-2.2a1 1 0 0 1 1-.25 11.4 11.4 0 0 0 3.6.57 1 1 0 0 1 1 1V20a1 1 0 0 1-1 1A17 17 0 0 1 3 4a1 1 0 0 1 1-1h3.5a1 1 0 0 1 1 1c0 1.250.2 2.45.57 3.57a1 1 0 0 1-.25 1Z" fill="#fff"/></svg>
      <strong>(800) 555-0142</strong></div>
    <div class="footer-web">
      <svg width="17" height="17" viewBox="0 0 24 24" fill="none" stroke="#fff" stroke-width="1.8"><circle cx="12" cy="12" r="9.5"/><ellipse cx="12" cy="12" rx="4" ry="9.5"/><path d="M2.5 12h19M4 7h16M4 17h16"/></svg>
      <strong>www.coastalflowline.com</strong></div>
  </footer>
</main>
</body>
</html>
```